Real Estate investment company needs billboard designs

This is our website: https://velmarkpropertygroup.com/
We are looking for some billboard concepts that uses our CEO in the design. I have attached some images and 1 billboard design that someone in our industry uses, but we don't want it exactly like his.

Industry/Entity Type

real estate

Colors

Designer to choose colors to be used in the design.

Requirements
Must have
• Company colors from websiute

```html
<!DOCTYPE html>
<html lang="en">
<head>
<meta charset="utf-8">
<title>Velmark Property Group – Billboard</title>
<link rel="stylesheet" href="https://fonts.googleapis.com/css2?family=Open+Sans:wght@600;700;800&display=swap">
<style>
  :root {
    --navy: #1a1838;
    --panel: #e1e1e4;
    --red: #d32f26;
    --white: #f2f2f2;
    --page: #eef1f3;
    --photo-top: #5b6270;
    --photo-bottom: #2a3040;
  }
  * { box-sizing: border-box; margin: 0; padding: 0; }
  html, body {
    width: 1200px; height: 1200px; overflow: hidden;
    background: var(--page);
    font-family: "Open Sans", Arial, sans-serif;
  }
  .billboard {
    position: absolute;
    left: 20px; top: 367px;
    width: 1310px; height: 525px;
    transform: scale(0.8855);
    transform-origin: top left;
    background: var(--navy);
    overflow: hidden;
  }
  .message-panel {
    position: absolute;
    left: 47px; top: 68px;
    width: 1193px; height: 387px;
    border-radius: 30px;
    overflow: hidden;
    background: var(--panel);
  }
  .message-panel__band {
    position: absolute;
    left: 0; right: 0; bottom: 0;
    height: 158px;
    background: var(--red);
  }
  .brand-tile {
    position: absolute;
    left: 120px; top: 0;
    width: 190px; height: 95px;
    background: var(--panel);
    box-shadow: 2px 3px 6px rgba(0,0,0,0.35);
    display: flex; flex-direction: column; justify-content: center;
    padding-left: 18px;
    color: var(--navy);
    font-weight: 800;
    font-size: 21px;
    line-height: 1.1;
  }
  .headline {
    position: absolute;
    left: 102px; top: 98px;
    font-size: 68px; font-weight: 600;
    color: var(--navy);
    letter-spacing: 0.5px;
    white-space: nowrap;
  }
  .call-line {
    position: absolute;
    left: 100px; top: 180px;
    font-size: 86px; font-weight: 700;
    color: var(--navy);
    letter-spacing: 5px;
    white-space: nowrap;
  }
  .question {
    position: absolute;
    left: 100px; top: 318px;
    font-size: 76px; font-weight: 700;
    color: var(--white);
    white-space: nowrap;
  }
  .web-address {
    position: absolute;
    left: 104px; top: 462px;
    font-size: 34px; font-weight: 600;
    color: var(--white);
    white-space: nowrap;
  }
  .ceo-photo {
    position: absolute;
    left: 1060px; top: 170px;
    width: 250px; height: 355px;
  }
</style>
</head>
<body>
  <div class="billboard">
    <div class="message-panel">
      <div class="message-panel__band"></div>
    </div>
    <div class="brand-tile">
      <span>Velmark</span>
      <span>Property Group</span>
    </div>
    <p class="headline">Get a Cash Offer, Same Day.</p>
    <p class="call-line">Call: 865-555-0147</p>
    <p class="question">Selling Your Home?</p>
    <p class="web-address">www.velmarkpropertygroup.com</p>
    <svg class="ceo-photo" role="img" aria-label="Photo of the company CEO smiling and pointing up at the phone number" viewBox="0 0 250 355">
      <defs>
        <linearGradient id="ceoTone" x1="0" y1="0" x2="0" y2="1">
          <stop offset="0" stop-color="var(--photo-top)"/>
          <stop offset="1" stop-color="var(--photo-bottom)"/>
        </linearGradient>
      </defs>
      <rect x="60" y="0" width="110" height="130" rx="40" fill="url(#ceoTone)"/>
      <rect x="0" y="110" width="250" height="245" rx="30" fill="url(#ceoTone)"/>
    </svg>
  </div>
</body>
</html>
```